Varga Lillas Physiotherapy Business Card Vienna

We need a business card design for a newly created Physiotherapy company based in Vienna Austria.
We seek a simple, modern, minimalist design without too much color variation. The font should look young/fresh, but definitely not childish or so. Since we are a starting Business, we currently haven't got a logo, if you feel like a logo would fit your design, feel free to use one, but it's not necessary.
Target Market(s)
Healthcare, young and elderly people with mobility issues
Industry/Entity Type
Health And Wellness
Contact Information for Business Card
Name: Lilla Varga
Title description: Physiotherapist
Phone num: +43 664 5290 4816
e-mail: lilla.praxis@brelomail.com
Colors
Designer to choose colors to be used in the design.
Requirements
Must have
- Final design language must be in German, basically, the Title Description needs to be "Physiotherapeutin" the other details remain as in the English Language.
Nice to have
- Simple, modern, minimalist design
Should not have
- too many colors, Obvious use of a skeleton, skull, spline

```html
<!DOCTYPE html>
<html lang="de">
<head>
<meta charset="utf-8">
<title>Varga Lillas Physiotherapy – Visitenkarte</title>
<link rel="stylesheet" href="https://fonts.googleapis.com/css2?family=Montserrat:wght@400;600;700&display=swap">
<style>
  :root {
    --backdrop: #d5d9d9;
    --card: #f3f2ef;
    --ink: #2a2a2a;
    --ink-soft: #3c3c3c;
    --rule: #4a4a4a;
    --shadow: rgba(0, 0, 0, 0.14);
  }
  * { box-sizing: border-box; margin: 0; padding: 0; }
  html, body {
    width: 1200px;
    height: 900px;
    overflow: hidden;
    background: var(--backdrop);
    font-family: "Montserrat", sans-serif;
    color: var(--ink);
  }
  .sheet {
    position: relative;
    width: 1200px;
    height: 900px;
  }
  .card {
    position: absolute;
    left: 270px;
    width: 660px;
    height: 377px;
    background: var(--card);
    box-shadow: 0 6px 18px var(--shadow);
  }
  .card--back { top: 48px; display: flex; align-items: center; justify-content: center; }
  .card--front { top: 475px; display: flex; align-items: center; padding: 0 48px; }

  .wordmark {
    color: var(--ink);
    line-height: 1;
  }
  .wordmark__name { display: block; font-weight: 700; text-transform: uppercase; letter-spacing: 0.02em; }
  .wordmark__field { display: block; font-weight: 400; text-transform: uppercase; margin-top: 4px; }

  .card--back .wordmark__name { font-size: 40px; }
  .card--back .wordmark__field { font-size: 20px; letter-spacing: 0.5em; }

  .card--front .wordmark__name { font-size: 27px; }
  .card--front .wordmark__field { font-size: 13.5px; letter-spacing: 0.48em; }

  .divider {
    width: 1.5px;
    height: 110px;
    background: var(--rule);
    margin: 0 28px 0 34px;
  }
  .contact { display: flex; flex-direction: column; }
  .contact__name { font-weight: 700; font-size: 22px; letter-spacing: 0.02em; }
  .contact__title { font-weight: 400; font-size: 14px; color: var(--ink-soft); margin: 2px 0 12px; }
  .contact__line {
    display: flex;
    align-items: center;
    gap: 8px;
    font-size: 14px;
    color: var(--ink-soft);
    line-height: 1.6;
  }
  .contact__icon { width: 11px; height: 11px; flex: none; }
</style>
</head>
<body>
<main class="sheet">
  <section class="card card--back" aria-label="Rückseite">
    <div class="wordmark">
      <span class="wordmark__name">Varga Lillas</span>
      <span class="wordmark__field">Physiotherapy</span>
    </div>
  </section>

  <section class="card card--front" aria-label="Vorderseite">
    <div class="wordmark">
      <span class="wordmark__name">Varga Lillas</span>
      <span class="wordmark__field">Physiotherapy</span>
    </div>
    <div class="divider"></div>
    <div class="contact">
      <p class="contact__name">Lilla Varga</p>
      <p class="contact__title">Physiotherapeutin</p>
      <p class="contact__line">
        <svg class="contact__icon" viewBox="0 0 12 12" aria-hidden="true">
          <path d="M3 1 L4.6 3.6 L3.6 4.8 Q4.6 7 7.2 8.4 L8.4 7.4 L11 9 L10 11 Q4 11 1 3 Z" fill="none" stroke="currentColor" stroke-width="1"/>
        </svg>
        +43 664 5290 4816
      </p>
      <p class="contact__line">
        <svg class="contact__icon" viewBox="0 0 12 12" aria-hidden="true">
          <rect x="1" y="2.5" width="10" height="7" fill="none" stroke="currentColor" stroke-width="1"/>
          <path d="M1 2.5 L6 6.5 L11 2.5" fill="none" stroke="currentColor" stroke-width="1"/>
        </svg>
        lilla.praxis@brelomail.com
      </p>
    </div>
  </section>
</main>
</body>
</html>
```